Hollowmere Capital Stationary Design

We have selected a logo as our winner, we now need a full stationary set to be in the same theme.
Required:
- Letter Head
- Business Card Template
- Custom Envelopes
- A5 Notepad Design (Front cover and content pages. Content pages blank(no lines) but with our branding on them,)
- With Compliments Slip
Updates

Hey All,

We have changed the colour scheme of our logo. Our apologies if anyone has begun designing based off the old scheme. Please see the updated scheme in the brief,

Oliver

Target Market(s)

Target market is experienced property developers and financial institutions.

Industry/Entity Type

Commercial Finance

Font styles to use
Serif

Colors
0054AA
0677BA
7BADD7
CADEEF
E8F1F8
0094D4
00A9DD
6FCCEA
C7EBF8
E9F6FB
00AB8E
00BBA5
67D7C9
C6EFE9
E9F9F6
59FF00
82FF00
B8FF75
E3FFCB
F4FFEA

```html
<!DOCTYPE html>
<html lang="en">
<head>
<meta charset="utf-8">
<title>Hollowmere Capital Stationery Set</title>
<link rel="stylesheet" href="https://fonts.googleapis.com/css2?family=Lato:wght@400;700&display=swap">
<style>
  :root {
    --brand-green: #1f8a45;
    --brand-blue: #1e3d9b;
    --ink-grey: #666a70;
    --paper: #ffffff;
    --backdrop: #2b2c2e;
  }
  * { box-sizing: border-box; margin: 0; padding: 0; }
  html, body { width: 1200px; height: 800px; overflow: hidden; }
  body {
    background: var(--backdrop);
    font-family: "Lato", sans-serif;
    position: relative;
  }
  .icons { position: absolute; width: 0; height: 0; }

  /* Shared sheet construction: green frame, white paper, white notch at the bottom */
  .sheet { position: absolute; background: var(--brand-green); }
  .sheet .paper { position: absolute; background: var(--paper); }
  .sheet .notch { position: absolute; bottom: 0; background: var(--paper); }
  .sheet .content { position: absolute; inset: 0; }

  /* Brand name wordmark in text font */
  .brand-name {
    position: absolute;
    color: var(--brand-blue);
    font-weight: 700;
    line-height: 1;
    text-align: center;
  }
  .brand-name span { display: block; }
  .brand-name .line-two { letter-spacing: 0.32em; margin-top: 0.18em; font-size: 0.55em; }

  .contact {
    position: absolute;
    display: grid;
    grid-template-columns: auto auto;
    column-gap: 1.4em;
    row-gap: 0.25em;
    color: var(--ink-grey);
  }
  .contact li { list-style: none; display: flex; align-items: center; gap: 0.35em; white-space: nowrap; }
  .contact svg { width: 1em; height: 1em; fill: var(--brand-blue); flex: none; }

  /* Letterhead */
  .letterhead { left: 159px; top: 37px; width: 342px; height: 442px; }
  .letterhead .paper { left: 11px; top: 12px; right: 11px; bottom: 11px; }
  .letterhead .notch { left: 58px; right: 58px; height: 11px; }
  .letterhead .brand-name { right: 24px; top: 27px; font-size: 15px; }
  .letterhead .contact { left: 22px; top: 407px; font-size: 6.6px; }

  /* Business card */
  .card { width: 166px; height: 95px; }
  .card .paper { left: 2px; top: 2px; right: 3px; bottom: 3px; }
  .card .notch { left: 26px; right: 28px; height: 3px; }
  .card-front { left: 54px; top: 129px; }
  .card-front .brand-name { right: 14px; top: 12px; font-size: 10px; }
  .card-front .holder {
    position: absolute; left: 6px; top: 63px; width: 134px;
    font-size: 5.6px; color: var(--brand-blue);
    padding-bottom: 3px; border-bottom: 0.5px solid #c9ccd1;
  }
  .card-front .holder .role { color: var(--ink-grey); font-size: 4.2px; }
  .card-front .contact { left: 6px; top: 78px; font-size: 4.2px; column-gap: 6px; }
  .card-back { left: 110px; top: 245px; }
  .card-back .brand-name { left: 0; right: 0; top: 35px; font-size: 12px; }

  /* Notepad pages */
  .notepad { top: 46px; width: 234px; height: 335px; }
  .notepad .paper { left: 11px; top: 11px; right: 11px; bottom: 11px; }
  .notepad .notch { left: 42px; right: 42px; height: 11px; }
  .notepad-branded { left: 580px; }
  .notepad-branded .brand-name { right: 20px; top: 19px; font-size: 14px; }
  .notepad-branded .contact { left: 17px; top: 306px; font-size: 5px; column-gap: 8px; }
  .notepad-cover { left: 869px; }

  /* DL envelope front */
  .envelope-front { left: 583px; top: 411px; width: 383px; height: 166px; }
  .envelope-front .paper { left: 9px; top: 8px; right: 9px; bottom: 9px; }
  .envelope-front .notch { left: 48px; right: 48px; height: 9px; }
  .envelope-front .brand-name { left: 23px; top: 24px; font-size: 13.5px; }
  .envelope-front .contact { left: 23px; top: 135px; font-size: 6.6px; grid-template-columns: auto; }

  /* With compliments slip */
  .compliments { left: 163px; top: 598px; width: 349px; height: 164px; }
  .compliments .paper { left: 9px; top: 8px; right: 9px; bottom: 9px; }
  .compliments .notch { left: 47px; right: 47px; height: 9px; }
  .compliments .brand-name { right: 24px; top: 21px; font-size: 15px; }
  .compliments .greeting {
    position: absolute; left: 19px; top: 97px;
    font-size: 11px; color: var(--brand-blue); font-weight: 400;
  }
  .compliments .contact { left: 19px; top: 128px; font-size: 6.6px; column-gap: 10px; }

  /* Envelope back */
  .envelope-back { position: absolute; left: 768px; top: 596px; width: 383px; height: 166px; }
</style>
</head>
<body>

<svg class="icons" aria-hidden="true">
  <defs>
    <symbol id="icon-phone" viewBox="0 0 16 16"><path d="M2 5c0-2 2-3 6-3s6 1 6 3v1h-3V5H5v1H2zM4 7h8l2 6H2z"/></symbol>
    <symbol id="icon-pin" viewBox="0 0 16 16"><path d="M8 1a5 5 0 0 0-5 5c0 4 5 9 5 9s5-5 5-9a5 5 0 0 0-5-5zm0 7a2 2 0 1 1 0-4 2 2 0 0 1 0 4z"/></symbol>
    <symbol id="icon-globe" viewBox="0 0 16 16"><path d="M8 1a7 7 0 1 0 0 14A7 7 0 0 0 8 1zm0 2c1 1 1.6 2.6 1.8 4H6.2C6.4 5.6 7 4 8 3zM3.1 9h3c.2 1.4.7 2.8 1.4 3.9A5 5 0 0 1 3.1 9zm6.4 3.9c.7-1.1 1.2-2.5 1.4-3.9h2A5 5 0 0 1 9.5 12.9z"/></symbol>
    <symbol id="icon-mail" viewBox="0 0 16 16"><path d="M2 7l6-5 6 5v7H2zm2 1v4h8V8L8 11z"/></symbol>
  </defs>
</svg>

<!-- Letterhead -->
<section class="sheet letterhead" aria-label="Letterhead">
  <div class="paper"></div><div class="notch"></div>
  <div class="content">
    <p class="brand-name"><span>HOLLOWMERE</span><span class="line-two">CAPITAL</span></p>
    <ul class="contact">
      <li><svg><use href="#icon-phone"/></svg>(00) 0000 0000</li>
      <li><svg><use href="#icon-globe"/></svg>www.hollowmerecapital.com</li>
      <li><svg><use href="#icon-pin"/></svg>11 dummy city, dummy place 00</li>
      <li><svg><use href="#icon-mail"/></svg>edwin@hollowmerecapital.com</li>
    </ul>
  </div>
</section>

<!-- Business card front -->
<section class="sheet card card-front" aria-label="Business card front">
  <div class="paper"></div><div class="notch"></div>
  <div class="content">
    <p class="brand-name"><span>HOLLOWMERE</span><span class="line-two">CAPITAL</span></p>
    <p class="holder">EDWIN HARLOW | <span class="role">Director</span></p>
    <ul class="contact">
      <li><svg><use href="#icon-phone"/></svg>(00) 0000 0000</li>
      <li><svg><use href="#icon-globe"/></svg>www.hollowmerecapital.com</li>
      <li><svg><use href="#icon-pin"/></svg>11 dummy city, dummy place 00</li>
      <li><svg><use href="#icon-mail"/></svg>edwin@hollowmerecapital.com</li>
    </ul>
  </div>
</section>

<!-- Business card back -->
<section class="sheet card card-back" aria-label="Business card back">
  <div class="paper"></div><div class="notch"></div>
  <div class="content">
    <p class="brand-name"><span>HOLLOWMERE</span><span class="line-two">CAPITAL</span></p>
  </div>
</section>

<!-- Notepad content page -->
<section class="sheet notepad notepad-branded" aria-label="Notepad content page">
  <div class="paper"></div><div class="notch"></div>
  <div class="content">
    <p class="brand-name"><span>HOLLOWMERE</span><span class="line-two">CAPITAL</span></p>
    <ul class="contact">
      <li><svg><use href="#icon-phone"/></svg>(00) 0000 0000</li>
      <li><svg><use href="#icon-globe"/></svg>www.hollowmerecapital.com</li>
      <li><svg><use href="#icon-pin"/></svg>11 dummy city, dummy place 00</li>
      <li><svg><use href="#icon-mail"/></svg>edwin@hollowmerecapital.com</li>
    </ul>
  </div>
</section>

<!-- Notepad plain page -->
<section class="sheet notepad notepad-cover" aria-label="Notepad page">
  <div class="paper"></div><div class="notch"></div>
</section>

<!-- DL envelope front -->
<section class="sheet envelope-front" aria-label="Envelope front">
  <div class="paper"></div><div class="notch"></div>
  <div class="content">
    <p class="brand-name"><span>HOLLOWMERE</span><span class="line-two">CAPITAL</span></p>
    <ul class="contact">
      <li><svg><use href="#icon-pin"/></svg>11 dummy city, dummy place 00</li>
    </ul>
  </div>
</section>

<!-- With compliments slip -->
<section class="sheet compliments" aria-label="With compliments slip">
  <div class="paper"></div><div class="notch"></div>
  <div class="content">
    <p class="brand-name"><span>HOLLOWMERE</span><span class="line-two">CAPITAL</span></p>
    <p class="greeting">With Compliments</p>
    <ul class="contact">
      <li><svg><use href="#icon-phone"/></svg>(00) 0000 0000</li>
      <li><svg><use href="#icon-globe"/></svg>www.hollowmerecapital.com</li>
      <li><svg><use href="#icon-pin"/></svg>11 dummy city, dummy place 00</li>
      <li><svg><use href="#icon-mail"/></svg>edwin@hollowmerecapital.com</li>
    </ul>
  </div>
</section>

<!-- Envelope back with flap -->
<svg class="envelope-back" viewBox="0 0 383 166" aria-label="Envelope back">
  <rect width="383" height="166" fill="var(--paper)"/>
  <path d="M0 0 Q10 24 22 30 L191 61 L362 30 Q374 24 383 0 Z" fill="var(--brand-green)"/>
</svg>

</body>
</html>
```